Business card design reauest

2 sided. White on both sides

Martin Oakhurst

Ho Chi Minh, Vietnam

Cell Phone / Whatsapp/ Wechat/Zalo
1-555-382-7194
Moakhurst@kvpartsline.vn
Www.kvpartsline.vn
Www.kvpartsline.com

Industry/Entity Type

Sofa and furniture and kitchen

Contact Information for Business Card

2 sided. White on both sides Martin Oakhurst Ho Chi Minh, Vietnam Cell Phone / Whatsapp/ Wechat/Zalo 1-555-382-7194 Moakhurst@kvpartsline.vn Www.kvpartsline.vn Www.kvpartsline.com

```html
<!DOCTYPE html>
<html lang="en">
<head>
<meta charset="utf-8">
<title>KV Partsline – Business Card</title>
<link rel="stylesheet" href="https://fonts.googleapis.com/css2?family=Source+Serif+4:wght@400;700&family=Noto+Serif:wght@400&display=swap">
<style>
  :root {
    --backdrop: #dedede;
    --card: #ffffff;
    --brand-green: #129a48;
    --ink: #231f20;
    --muted: #6d6d6d;
    --rule: #9a9a9a;
  }
  * { margin: 0; padding: 0; box-sizing: border-box; }
  html, body {
    width: 1200px; height: 1200px; overflow: hidden;
    background: var(--backdrop);
  }
  .canvas { position: relative; width: 1200px; height: 1200px; }
  .card {
    position: absolute; left: 179px; width: 862px; height: 496px;
    background: var(--card);
  }
  .card--front { top: 84px; }
  .card--back { top: 621px; }

  .brand {
    position: absolute; display: flex; align-items: center; gap: 12px;
    font-family: "Source Serif 4", Georgia, serif; font-weight: 400;
    color: var(--brand-green); letter-spacing: 1px; white-space: nowrap;
  }
  .brand__mark { background: var(--brand-green); flex: none; }
  .card--front .brand {
    left: 50%; top: 50%; transform: translate(-50%, -50%);
    font-size: 38px;
  }
  .card--front .brand__mark { width: 22px; height: 22px; }
  .card--back .brand {
    right: 96px; top: 130px; font-size: 23px;
  }
  .card--back .brand__mark { width: 14px; height: 14px; }

  .person {
    position: absolute; left: 94px; top: 236px;
    font-family: "Source Serif 4", Georgia, serif;
  }
  .person__name {
    font-size: 31px; font-weight: 700; color: var(--brand-green); line-height: 1;
  }
  .person__role {
    margin-top: 3px; font-size: 17px; font-weight: 400; color: var(--muted);
    letter-spacing: 1px; line-height: 1;
  }
  .location {
    position: absolute; right: 96px; top: 270px;
    font-family: "Source Serif 4", Georgia, serif; font-size: 19px; color: var(--muted);
    line-height: 1;
  }
  .divider {
    position: absolute; left: 94px; width: 672px; top: 292px;
    height: 1px; background: var(--rule);
  }
  .contacts {
    position: absolute; left: 94px; top: 293px; list-style: none;
    font-family: "Noto Serif", Georgia, serif; font-size: 17px; color: var(--ink);
    letter-spacing: 2px;
  }
  .contacts__item {
    display: flex; align-items: center; gap: 9px; height: 32px; white-space: nowrap;
  }
  .contacts__icon { width: 20px; height: 20px; flex: none; }
  .contacts__note {
    color: var(--brand-green); font-size: 15px; letter-spacing: 1.5px; margin-left: 4px;
  }
</style>
</head>
<body>
<div class="canvas">

  <section class="card card--front" aria-label="Card front">
    <div class="brand"><span class="brand__mark"></span>KV PARTSLINE</div>
  </section>

  <section class="card card--back" aria-label="Card back">
    <div class="brand"><span class="brand__mark"></span>KV PARTSLINE</div>

    <div class="person">
      <p class="person__name">Martin Oakhurst</p>
      <p class="person__role">FOUNDER</p>
    </div>
    <p class="location">Ho Chi Minh, Vietnam</p>
    <div class="divider"></div>

    <ul class="contacts">
      <li class="contacts__item">
        <svg class="contacts__icon" viewBox="0 0 20 20" aria-hidden="true">
          <rect width="20" height="20" fill="#231f20"/>
          <path d="M6 4 l3 0 l1 4 l-2 1 q1 3 3 4 l1 -2 l4 1 l0 3 q-7 1 -10 -11z" fill="#fff"/>
        </svg>
        <span>1-555-382-7194</span><span class="contacts__note">Mobile/Chat/Text</span>
      </li>
      <li class="contacts__item">
        <svg class="contacts__icon" viewBox="0 0 20 20" aria-hidden="true">
          <rect width="20" height="20" fill="#231f20"/>
          <rect x="4" y="6" width="12" height="8" fill="none" stroke="#fff" stroke-width="1.2"/>
          <path d="M4 6 l6 5 l6 -5 M4 14 l4.5 -4 M16 14 l-4.5 -4" fill="none" stroke="#fff" stroke-width="1.2"/>
        </svg>
        <span>moakhurst@kvpartsline.vn</span>
      </li>
      <li class="contacts__item">
        <svg class="contacts__icon" viewBox="0 0 20 20" aria-hidden="true">
          <rect width="20" height="20" fill="#231f20"/>
          <circle cx="10" cy="10" r="6" fill="none" stroke="#fff" stroke-width="1.4"/>
          <ellipse cx="10" cy="10" rx="2.5" ry="6" fill="none" stroke="#fff" stroke-width="1"/>
          <path d="M4 10 h12" stroke="#fff" stroke-width="1"/>
        </svg>
        <span>www.kvpartsline.vn</span>
      </li>
      <li class="contacts__item">
        <svg class="contacts__icon" viewBox="0 0 20 20" aria-hidden="true">
          <rect width="20" height="20" fill="#231f20"/>
          <circle cx="10" cy="10" r="6" fill="none" stroke="#fff" stroke-width="1.4"/>
          <ellipse cx="10" cy="10" rx="2.5" ry="6" fill="none" stroke="#fff" stroke-width="1"/>
          <path d="M4 10 h12" stroke="#fff" stroke-width="1"/>
        </svg>
        <span>www.kvpartsline.com</span>
      </li>
    </ul>
  </section>

</div>
</body>
</html>
```